Product label for herbal salves, lotions, soaps and tinctures

We need a very simple, clean and organic looking label that can be used for an ointment jar, a lotion bottle and a dropper bottle.
We have an existing logo (see attached). We like the colors white, olive green, gold and black. It needs to include product name as dominant and logo. It also needs to include an ingredient list, and usage statement. Include weight of product, distributed by, made in the USA, and NQB statement.
Example of what needs to be present:
Logo
Name: Calmwick Balm
Used for: For Muscle Aches, Arthritis, Tendonitis, Headaches
To Use: For muscle aches, arthritis and tendonitis, massage into affected area. For tension headache apply to neck, temples and forehead.
Store in a cool and dry place, away from direct heat and sunlight.
Weight of product: 1.75
DIST. BY: Brookmere Herbal
Made in the USA
This product is not intended to diagnose, treat, cure
or prevent any disease. Not regulated
by the NQB. Please consult your health care practitioner
before using product. Discontinue use if any adverse reaction occurs.
Ingredient list:
Wildcrafted Ingredients:
Ashwagandha Root, Peppermint Leaf, Hops Flowers, St. John’s Wort Herb, Arnica Flowers, Green Tea Leaf, Alfalfa Leaf, Dandelion Root, Burdock Root, Chickweed Herb, Chaparral Leaf, Yarrow Flowers, Boneset Herb, Moringa Leaf, Meadowsweet Herb, Nettle Leaf
Organic Ingredients:
Olive Oil, Aloe Leaf, Sweet Birch Bark, Helichrysum Flowers, Holy Basil Leaf, Borage Herb, Ginger Root, Angelica Root, White Willow Bark, Mustard Seed, Beeswax, Vitamin E, Essential Oils
Dimensions of Jar:
Circumference: 7 in.
Height: 1 in.

```html
<!DOCTYPE html>
<html lang="en">
<head>
<meta charset="UTF-8">
<title>Brookmere Herbal – Calmwick Balm Label</title>
<link href="https://fonts.googleapis.com/css2?family=Josefin+Sans:wght@400;600;700&family=Open+Sans:wght@400;600;700&display=swap" rel="stylesheet">
<style>
  :root {
    --backdrop: #d8d4d4;
    --label: #ffffff;
    --olive: #4b5a22;
    --olive-dark: #3e4a1b;
    --gold: #b5832a;
    --ink: #222222;
    --ink-soft: #3a3a3a;
    --rule: #e4e1da;
  }
  * { box-sizing: border-box; margin: 0; padding: 0; }
  html, body {
    width: 1200px; height: 900px; overflow: hidden;
    background: var(--backdrop);
  }
  body {
    display: flex; align-items: center; justify-content: center;
    font-family: "Open Sans", Arial, sans-serif; color: var(--ink);
  }
  .label {
    width: 1120px; height: 520px;
    background: var(--label);
    border-radius: 6px;
    display: grid;
    grid-template-columns: 400px 380px 340px;
    box-shadow: 0 2px 10px rgba(0,0,0,.08);
  }
  .panel { padding: 48px 36px; position: relative; }
  .panel + .panel { border-left: 1px dashed var(--rule); }

  /* Front */
  .front { display: flex; flex-direction: column; align-items: center; text-align: center; }
  .brand { display: flex; align-items: center; gap: 10px; margin-top: 20px; }
  .brand-dot { width: 16px; height: 16px; border-radius: 50%; background: var(--gold); }
  .brand-name {
    font-family: "Josefin Sans", sans-serif; font-weight: 700;
    font-size: 34px; color: var(--olive); letter-spacing: .5px;
  }
  .product-name { margin-top: 64px; font-family: "Josefin Sans", sans-serif; color: #4a4340; }
  .product-name .line-1 { display: block; font-size: 32px; font-weight: 600; letter-spacing: 1px; }
  .product-name .line-2 { display: block; font-size: 84px; font-weight: 600; letter-spacing: 3px; line-height: 1; margin-top: 6px; }
  .uses {
    margin-top: 22px; background: var(--olive); color: #fff;
    font-family: "Josefin Sans", sans-serif; font-weight: 600; font-size: 17px;
    padding: 8px 14px; border-radius: 3px;
  }
  .net-weight { margin-top: auto; font-size: 14px; font-weight: 600; color: var(--ink); }

  /* Ingredients */
  .ingredients .brand { margin-top: 0; margin-bottom: 26px; }
  .ingredients .brand-name { font-size: 22px; }
  .ingredients .brand-dot { width: 11px; height: 11px; }
  .ingredients h2 {
    font-family: "Josefin Sans", sans-serif; font-weight: 700;
    font-size: 18px; color: var(--ink); margin: 18px 0 8px;
  }
  .ingredients p { font-size: 12.5px; line-height: 1.6; color: var(--ink-soft); }

  /* Directions */
  .directions h2 {
    font-family: "Josefin Sans", sans-serif; font-weight: 700;
    font-size: 18px; margin-bottom: 8px; color: var(--ink);
  }
  .directions p { font-size: 12.5px; line-height: 1.6; color: var(--ink-soft); }
  .directions .storage { margin-top: 14px; }
  .directions .distribution { margin-top: 14px; font-weight: 600; color: var(--ink); }
  .disclaimer {
    margin-top: 18px; background: var(--gold); color: #fff;
    padding: 12px 14px; border-radius: 3px;
  }
  .disclaimer p { color: #fff; font-size: 11.5px; line-height: 1.55; }
  .disclaimer p + p { margin-top: 8px; }
</style>
</head>
<body>
  <main class="label">
    <section class="panel front">
      <div class="brand">
        <span class="brand-dot"></span>
        <span class="brand-name">Brookmere Herbal</span>
      </div>
      <h1 class="product-name">
        <span class="line-1">CALMWICK</span>
        <span class="line-2">BALM</span>
      </h1>
      <div class="uses">For Muscle Aches, Arthritis, Tendonitis, Headaches</div>
      <div class="net-weight">Net Weight : 1.75gm.</div>
    </section>

    <section class="panel ingredients">
      <div class="brand">
        <span class="brand-dot"></span>
        <span class="brand-name">Brookmere Herbal</span>
      </div>
      <h2>Wildcrafted Ingredients:</h2>
      <p>Ashwagandha Root, Peppermint Leaf, Hops Flowers, St. John’s Wort Herb, Arnica Flowers, Green Tea Leaf, Alfalfa Leaf, Dandelion Root, Burdock Root, Chickweed Herb, Chaparral Leaf, Yarrow Flowers, Boneset Herb, Moringa Leaf, Meadowsweet Herb, Nettle Leaf</p>
      <h2>Organic Ingredients:</h2>
      <p>Olive Oil, Aloe Leaf, Sweet Birch Bark, Helichrysum Flowers, Holy Basil Leaf, Borage Herb, Ginger Root, Angelica Root, White Willow Bark, Mustard Seed, Beeswax, Vitamin E, Essential Oils</p>
    </section>

    <section class="panel directions">
      <h2>To Use:</h2>
      <p>For muscle aches, arthritis and tendonitis, massage into affected area. For tension headache apply to neck, temples and forehead.</p>
      <p class="storage">Store in a cool and dry place, away from direct heat and sunlight.</p>
      <p class="distribution">DIST. BY: Brookmere Herbal<br>Made in the USA</p>
      <div class="disclaimer">
        <p>This product is not intended to diagnose, treat, cure or prevent any disease.</p>
        <p>Not regulated by the NQB. Please consult your health care practitioner before using product. Discontinue use if any adverse reaction occurs.</p>
      </div>
    </section>
  </main>
</body>
</html>
```